QV - menu design

Hi,

We require elegant menu design for upscale restaurant. Please find attached the logo and the menu items for your reference.

for inspiration, this is a good website: -
http://www.platewhisper.example/bellfoldnotes/about.php

We are very much open for Menu Size suggestions.

unfortunately the place is going under renovation, we don't have updated images to it. the closest look and feel to our place is http://varnelo.example ..

we are also open for creative options on the shape, the styles, etc. as long as it represents the fine dine feel ...

Thanks ...

Dear All,

We wouldlike to extend our apology for not being able to provide feedbacks on everysingle design. We were extremely busy and we have multiple contests opensimultaneously which makes the process even harder.

However,we would like to thank you all for the efforts you have put into designingour menu. It is very much appreciated …

We wishyou all success in your design ventures and we are quite positive that we willbe working with many of you on many projects in the soon future. 

Thanks & Regards,

TLG Team...

 

 

 

Industry/Entity Type

Restaurant

Requirements
Must have
• Please ensure that there are 'some' images in the menu ... this is very important.
Should not have
• IMPORTANT: -

1. Please DO NOT insert any currency sign to the menu
2. Please keep the prices of the menu at the end of the menu items descriptions NOT beside the menu item names. The font of the price should be similar to the menu item description and please DO NOT bold the numbers. the prices should be subtle.

Thank you ...

```html
<!DOCTYPE html>
<html lang="en">
<head>
<meta charset="utf-8">
<title>Menu: Soup and Salads</title>
<link rel="stylesheet" href="https://fonts.googleapis.com/css2?family=Questrial&family=Didact+Gothic&display=swap">
<style>
  :root {
    --soup-panel: #2d241f;
    --salad-panel: #1b2018;
    --heading-tan: #b99b79;
    --item-name: #f1ece3;
    --item-desc: #d3ccc0;
    --wood-light: #a58a70;
    --wood-dark: #5a4535;
    --broth: #c98a45;
    --leaf-green: #6e9b3e;
    --plate-white: #eef0ec;
    --page-bg: #ffffff;
  }
  * { margin: 0; padding: 0; box-sizing: border-box; }
  html, body { width: 1200px; height: 720px; overflow: hidden; background: var(--page-bg); }
  .menu-spread { position: relative; width: 1200px; height: 720px; overflow: hidden; font-family: "Didact Gothic", sans-serif; }

  .page { position: absolute; top: 0; height: 720px; overflow: hidden; }
  .page--soup { left: 0; width: 600px; }
  .page--salads { left: 603px; width: 597px; }

  .photo { position: absolute; }
  .photo--soup-bowl {
    inset: 0;
    background:
      radial-gradient(ellipse 300px 210px at 290px 420px, var(--broth) 0%, #b57a3e 45%, #6e6a60 70%, transparent 72%),
      linear-gradient(160deg, var(--wood-light) 0%, #8a715b 50%, var(--wood-dark) 100%);
  }
  .photo--salad-plate {
    left: 0; top: 0; width: 597px; height: 300px;
    background:
      radial-gradient(ellipse 330px 150px at 400px 120px, var(--leaf-green) 0%, #8db25a 40%, var(--plate-white) 62%, transparent 66%),
      linear-gradient(180deg, #dcdcd6 0%, #c9cfc2 60%, #7fa045 100%);
  }

  .item-panel { position: absolute; }
  .item-panel--soup { left: 128px; top: 0; width: 472px; height: 197px; background: var(--soup-panel); }
  .item-panel--salads { left: 0; top: 285px; width: 597px; height: 435px; background: var(--salad-panel); }

  .section-tab {
    position: absolute;
    font-family: "Questrial", sans-serif;
    font-weight: 400;
    color: var(--heading-tan);
    font-size: 35px;
    line-height: 1;
    display: flex; align-items: center; justify-content: center;
  }
  .section-tab--soup { left: 378px; top: 180px; width: 172px; height: 56px; background: var(--soup-panel); }
  .section-tab--salads { left: 385px; top: 281px; width: 170px; height: 50px; background: var(--salad-panel); }

  .dish-list { position: absolute; list-style: none; }
  .dish-list--soup { left: 40px; top: 33px; width: 420px; }
  .dish-list--salads { left: 56px; top: 43px; width: 530px; }

  .dish__name {
    font-family: "Questrial", sans-serif;
    font-weight: 400;
    color: var(--item-name);
    font-size: 16px;
    line-height: 20px;
    letter-spacing: 0.3px;
  }
  .dish__desc {
    color: var(--item-desc);
    font-size: 9.5px;
    line-height: 13px;
    margin-top: 4px;
    letter-spacing: 0.25px;
  }
  .dish-list--soup .dish + .dish { margin-top: 9.5px; }
  .dish-list--salads .dish__name { font-size: 16.5px; }
  .dish-list--salads .dish__desc { margin-top: 5px; font-size: 10.3px; white-space: nowrap; }
  .dish-list--salads .dish + .dish { margin-top: 11.6px; }
</style>
</head>
<body>
<main class="menu-spread">
  <section class="page page--soup" aria-label="Soup">
    <div class="photo photo--soup-bowl" role="img" aria-label="Bowl of seafood soup with prawns and herbs on a rustic wooden table"></div>
    <div class="item-panel item-panel--soup">
      <ul class="dish-list dish-list--soup">
        <li class="dish">
          <h3 class="dish__name">Bouillabaisse</h3>
          <p class="dish__desc">Traditional French Seafood soup, with Saffron and Estragon. 119</p>
        </li>
        <li class="dish">
          <h3 class="dish__name">Barley soup</h3>
          <p class="dish__desc">With fresh vegetables, tomato smoothie and a hint of garlic oil. 49</p>
        </li>
        <li class="dish">
          <h3 class="dish__name">Beef chili</h3>
          <p class="dish__desc">Served with Arabic bread, fresh guacamole and spicy black beans. 49</p>
        </li>
      </ul>
    </div>
    <h2 class="section-tab section-tab--soup">Soup</h2>
  </section>

  <section class="page page--salads" aria-label="Salads">
    <div class="photo photo--salad-plate" role="img" aria-label="Plate of fresh green salad with tomatoes, cucumber, olives and feta, with a fork"></div>
    <div class="item-panel item-panel--salads">
      <ul class="dish-list dish-list--salads">
        <li class="dish">
          <h3 class="dish__name">Vegetarian Salad</h3>
          <p class="dish__desc">Fresh green leaves, Italian cherry tomatoes, carrots, cucumber, green apple and toasted pine nuts<br>with our special grain mustard dressing.59</p>
        </li>
        <li class="dish">
          <h3 class="dish__name">Sweet Gorgonzola Cheese Salad</h3>
          <p class="dish__desc">Fresh green leaves, Gorgonzola cheese, fresh pears, walnuts, garlic bread croutons, green celery<br>with smoked honey dressing.59</p>
        </li>
        <li class="dish">
          <h3 class="dish__name">Beef Sirloin Salad</h3>
          <p class="dish__desc">Fresh green leaves, beef sirloin julienne, caramelized apples, Parmesan cheese, toasted almonds,<br>sundried tomatoes and light Pesto sauce.79</p>
        </li>
        <li class="dish">
          <h3 class="dish__name">Tandoori Chicken Salad</h3>
          <p class="dish__desc">Fresh green leaves, Tandoori chicken breast, fresh mango, fresh goat cheese, crispy chicken skin<br>and Jasmine rice sauce.69</p>
        </li>
        <li class="dish">
          <h3 class="dish__name">Sea food Salad</h3>
          <p class="dish__desc">Fresh green leaves, fresh steamed seafood, black olives, celery, garlic bread croutons, avocado<br>and grapefruit dressing.89</p>
        </li>
        <li class="dish">
          <h3 class="dish__name">Fresh Tuna Salad</h3>
          <p class="dish__desc">Fresh green leaves, low temperature cooked tuna, taggiasca olives, red onions, roasted peppers,<br>soy marinated tofu and lemon dressing.89</p>
        </li>
      </ul>
    </div>
    <h2 class="section-tab section-tab--salads">Salads</h2>
  </section>
</main>
</body>
</html>
```